Creative Design "Size Chart" for a Clothing Product

Hi, My dear friends! I am looking to do a contest to design a unique creative "Size Chart" for our clothing line. See Attached the Sizes & Ideas Thanks Good Luck Osvald

Colors

Designer to choose colors to be used in the design.

```html
<!DOCTYPE html>
<html lang="en">
<head>
<meta charset="utf-8">
<title>Size Chart</title>
<link href="https://fonts.googleapis.com/css2?family=Quicksand:wght@400;500;600&display=swap" rel="stylesheet">
<style>
  :root {
    --teal: #38a1bf;
    --magenta: #c46197;
    --ink: #4b4848;
    --value: #5a5858;
    --row-grey: #e6e6e6;
    --rule: #9c9c9c;
    --red: #e03a3a;
    --page: #ffffff;
    --backdrop: #f6f6f6;
  }
  * { box-sizing: border-box; margin: 0; padding: 0; }
  html, body {
    width: 1200px; height: 1200px; overflow: hidden;
    background: var(--backdrop);
    font-family: "Quicksand", "Varela Round", sans-serif;
  }
  .page {
    position: absolute; left: 223px; top: 66px;
    width: 761px; height: 1075px;
    background: var(--page);
  }
  .stage { position: absolute; left: -223px; top: -66px; width: 1200px; height: 1200px; }

  .heading-rule {
    position: absolute; left: 299px; width: 610px; height: 3px; background: var(--ink);
  }
  .heading-tab {
    position: absolute; background: var(--ink); color: #fff;
    border-radius: 18px 18px 0 0;
    display: flex; align-items: center; justify-content: center;
    font-weight: 500;
  }
  .title-tab { left: 436px; top: 105px; width: 336px; height: 63px; font-size: 50px; letter-spacing: 0.5px; }
  .title-rule { top: 165px; }
  .measure-tab { left: 487px; top: 825px; width: 233px; height: 43px; font-size: 30px; border-radius: 14px 14px 0 0; }
  .measure-rule { top: 866px; }

  .size-table {
    position: absolute; left: 299px;
    display: grid;
    grid-template-rows: 42px 41px 41px;
  }
  .size-table.six { grid-template-columns: 158px repeat(6, 65px); }
  .size-table.seven { grid-template-columns: 158px repeat(7, 65px); }
  .men { top: 217px; --accent: var(--teal); }
  .women { top: 369px; --accent: var(--magenta); }
  .boys { top: 521px; --accent: var(--teal); }
  .girls { top: 673px; --accent: var(--magenta); }

  .group-label {
    background: var(--accent); color: #fff;
    border-radius: 0 12px 0 0;
    font-size: 30px; font-weight: 500;
    display: flex; align-items: center; padding-left: 13px; padding-top: 2px;
  }
  .size {
    color: var(--accent); font-size: 20px; font-weight: 500;
    border-bottom: 3px solid var(--accent);
    display: flex; flex-direction: column; align-items: center; justify-content: center;
    line-height: 1;
  }
  .size + .size { border-left: 1.5px solid var(--rule); }
  .size small { font-size: 11px; margin-top: 2px; font-weight: 500; }
  .row-label {
    color: var(--accent); font-size: 20px; font-weight: 500;
    display: flex; align-items: center; justify-content: flex-end; padding-right: 22px;
  }
  .val {
    color: var(--value); font-size: 17.5px; font-weight: 500;
    border-left: 1.5px solid var(--rule);
    display: flex; align-items: center; justify-content: center;
  }
  .waist { background: var(--row-grey); }

  .figure-area {
    position: absolute; left: 284px; top: 906px; width: 422px; height: 194px;
    background: linear-gradient(90deg, #e4e4e4, #dcdcdc 50%, #e4e4e4);
    border-radius: 6px;
  }
  .guide {
    position: absolute; left: 740px; width: 1.5px; background: var(--red);
  }
  .guide.chest { top: 908px; height: 96px; }
  .guide.waist-line { top: 1046px; height: 52px; }
  .note { position: absolute; left: 750px; color: var(--ink); }
  .note h3 { font-size: 19px; font-weight: 500; line-height: 1; letter-spacing: 0.3px; }
  .note p { font-size: 12.3px; line-height: 15.8px; font-weight: 500; margin-top: 2px; }
  .note.chest-note { top: 906px; width: 180px; }
  .note.waist-note { top: 1045px; }
  .note.waist-note p { font-size: 15.5px; line-height: 19px; }
</style>
</head>
<body>
<div class="stage">
  <div class="page" style="left:223px;top:66px;position:absolute"></div>

  <div class="heading-rule title-rule"></div>
  <div class="heading-tab title-tab">Size Chart</div>

  <div class="size-table six men">
    <div class="group-label">Mens</div>
    <div class="size">S</div><div class="size">M</div><div class="size">L</div><div class="size">XL</div><div class="size">2X</div><div class="size">3X</div>
    <div class="row-label">Chest</div>
    <div class="val">34-36</div><div class="val">36-38</div><div class="val">38-40</div><div class="val">40-42</div><div class="val">43-45</div><div class="val">45-48</div>
    <div class="row-label waist">Waist</div>
    <div class="val waist">28-30</div><div class="val waist">30-32</div><div class="val waist">32-34</div><div class="val waist">34-36</div><div class="val waist">36-40</div><div class="val waist">40-44</div>
  </div>

  <div class="size-table seven women">
    <div class="group-label">Womens</div>
    <div class="size">XS<small>(0-2)</small></div><div class="size">S<small>(4-6)</small></div><div class="size">M<small>(8-10)</small></div><div class="size">L<small>(12-14)</small></div><div class="size">XL<small>(14-16)</small></div><div class="size">2X<small>(18)</small></div><div class="size">3X<small>(20)</small></div>
    <div class="row-label">Chest</div>
    <div class="val">32-34</div><div class="val">34-36</div><div class="val">36-38</div><div class="val">38-40</div><div class="val">40-42</div><div class="val">42-44</div><div class="val">44-46</div>
    <div class="row-label waist">Waist</div>
    <div class="val waist">26-28</div><div class="val waist">28-30</div><div class="val waist">30-32</div><div class="val waist">32-34</div><div class="val waist">34-36</div><div class="val waist">36-38</div><div class="val waist">38-40</div>
  </div>

  <div class="size-table six boys">
    <div class="group-label">Boys</div>
    <div class="size">XXS</div><div class="size">XS</div><div class="size">S</div><div class="size">M</div><div class="size">L</div><div class="size">XL</div>
    <div class="row-label">Chest</div>
    <div class="val">20-23</div><div class="val">23-26</div><div class="val">26-29</div><div class="val">29-32</div><div class="val">32-35</div><div class="val">35-38</div>
    <div class="row-label waist">Waist</div>
    <div class="val waist">19-21</div><div class="val waist">21-23</div><div class="val waist">23-25</div><div class="val waist">25-27</div><div class="val waist">27-29</div><div class="val waist">29-31</div>
  </div>

  <div class="size-table six girls">
    <div class="group-label">Girls</div>
    <div class="size">XXS</div><div class="size">XS</div><div class="size">S</div><div class="size">M</div><div class="size">L</div><div class="size">XL</div>
    <div class="row-label">Chest</div>
    <div class="val">19-22</div><div class="val">22-25</div><div class="val">25-28</div><div class="val">28-31</div><div class="val">31-34</div><div class="val">34-37</div>
    <div class="row-label waist">Waist</div>
    <div class="val waist">18-20</div><div class="val waist">20-22</div><div class="val waist">22-24</div><div class="val waist">24-26</div><div class="val waist">26-28</div><div class="val waist">28-30</div>
  </div>

  <div class="heading-rule measure-rule"></div>
  <div class="heading-tab measure-tab">Measurement</div>

  <div class="figure-area" role="img" aria-label="Outline figures of a man, woman, boy and girl with red guide lines marking chest and waist measurement points"></div>

  <div class="guide chest"></div>
  <div class="note chest-note">
    <h3>CHEST</h3>
    <p>Measure your chest around the back and across your bust for women/girl, or the largest part of your chest for men/boy going under your arms.</p>
  </div>

  <div class="guide waist-line"></div>
  <div class="note waist-note">
    <h3>WAIST</h3>
    <p>Measure around your<br>natural waistline.</p>
  </div>
</div>
</body>
</html>
```